Plakate für Psychologische Beratung am Telefon
Zielgruppe
Psychologische Beratung am Telefon
Aufgabenstellung
anliegendes Word Dokument soll als eine Art 'Plakat' (pdf Datei) erstellt werden. Diese PDF Datei wird dann an alle MitarbeiterInnen gesandt und soll Auskunft über das Beratungsangebot geben. Die Farben bitte so wie auf dieser Website (das ist unser Mutterunternehmen). www.lindenhof-kolleg.com.

```html
<!DOCTYPE html>
<html lang="de">
<head>
<meta charset="utf-8">
<title>Anonymes Beratungs- und Begleitangebot</title>
<link rel="stylesheet" href="https://fonts.googleapis.com/css2?family=Oswald:wght@300;400;500;700&family=Montserrat:wght@400;500;700&display=swap">
<style>
  :root {
    --bg: #d8cbb1;
    --paper: #ffffff;
    --teal: #3a93b4;
    --teal-light: #46a9c8;
    --navy: #24607f;
    --mist: rgba(188, 219, 231, 0.82);
    --ink: #141414;
    --text: #2b2b2b;
    --photo-a: #dfe3e8;
    --photo-b: #c9ced6;
  }
  * { box-sizing: border-box; margin: 0; padding: 0; }
  html, body { width: 1200px; height: 1129px; overflow: hidden; background: var(--bg); }
  .poster {
    position: absolute; left: 218px; top: 24px; width: 764px; height: 1080px;
    background: var(--paper); overflow: hidden;
    font-family: "Montserrat", sans-serif; color: var(--text);
  }
  .shapes { position: absolute; inset: 0; }
  .brand {
    position: absolute; left: 50px; top: 70px; display: flex; align-items: center; gap: 10px;
    font-family: "Montserrat", sans-serif; font-weight: 500; font-size: 17px; letter-spacing: 2px;
    color: var(--ink); text-transform: uppercase;
  }
  .brand-dot { width: 16px; height: 16px; border-radius: 50%; background: var(--navy); }
  .headline {
    position: absolute; left: 330px; top: 36px;
    font-family: "Oswald", sans-serif; font-weight: 400; color: var(--ink);
    font-size: 58px; line-height: 1.0; text-transform: uppercase;
  }
  .headline strong { font-weight: 700; }
  .subline {
    position: absolute; left: 330px; top: 350px; width: 420px;
    font-family: "Oswald", sans-serif; font-weight: 400; font-size: 18px; line-height: 1.3; color: var(--ink);
  }
  .hotline-intro {
    position: absolute; left: 380px; top: 436px; font-size: 14px; letter-spacing: 1px; line-height: 1.35; color: #333;
  }
  .hotline-band {
    position: absolute; left: 380px; top: 480px; width: 384px; height: 50px;
    background: var(--navy); display: flex; align-items: center; gap: 14px; padding-left: 16px;
    color: #fff; font-family: "Oswald", sans-serif; font-weight: 500; font-size: 30px; letter-spacing: 1px;
  }
  .hours { position: absolute; left: 390px; top: 548px; font-size: 15px; line-height: 1.3; color: #222; letter-spacing: .5px; }
  .hours p + p { margin-top: 8px; }
  .audience {
    position: absolute; left: 400px; top: 668px;
    font-family: "Oswald", sans-serif; font-size: 17px; line-height: 1.35; color: #111;
  }
  .bar {
    position: absolute; height: 30px; background: var(--navy); color: #fff;
    font-family: "Oswald", sans-serif; font-weight: 500; font-size: 18px;
    display: flex; align-items: center; justify-content: flex-end; padding-right: 14px;
  }
  .bar-fields { left: 0; top: 740px; width: 390px; }
  .bar-process { left: 0; top: 850px; width: 430px; }
  .bar-anon { left: 40px; top: 950px; width: 450px; }
  .field { position: absolute; top: 780px; width: 170px; font-size: 9px; line-height: 1.4; color: #444; }
  .field h3 { font-size: 12px; font-weight: 700; color: #111; margin-bottom: 4px; line-height: 1.2; }
  .field-private { left: 250px; }
  .field-health { left: 432px; top: 770px; }
  .field-work { left: 600px; top: 760px; width: 160px; }
  .process { position: absolute; left: 300px; top: 886px; width: 440px; font-size: 9px; line-height: 1.45; color: #333; }
  .process h3 { font-size: 13px; font-weight: 700; color: #111; margin-bottom: 3px; }
  .anon-note { position: absolute; left: 300px; top: 988px; font-size: 9px; color: #333; }
  .footer-band {
    position: absolute; left: 0; bottom: 0; width: 100%; height: 64px; background: var(--teal-light);
    color: #fff; font-family: "Oswald", sans-serif; font-weight: 700; font-size: 16px; line-height: 1.3;
    letter-spacing: .5px; text-align: center; padding-top: 10px;
  }
</style>
</head>
<body>
<main class="poster">
  <svg class="shapes" viewBox="0 0 764 1080" width="764" height="1080">
    <polygon points="0,280 300,280 520,600 300,930 0,930" fill="url(#photoTone)" role="img" aria-label="Foto: Beraterin mit Headset am Telefonarbeitsplatz"/>
    <defs>
      <linearGradient id="photoTone" x1="0" y1="0" x2="1" y2="1">
        <stop offset="0" stop-color="#2e3a56"/>
        <stop offset="0.35" stop-color="#c9ced6"/>
        <stop offset="1" stop-color="#eef0f2"/>
      </linearGradient>
    </defs>
    <polygon points="250,150 380,150 764,520 764,560 620,560" fill="var(--teal)"/>
    <polygon points="620,560 764,560 420,1010 290,1010" fill="var(--teal)"/>
    <polygon points="370,430 764,430 764,500 640,760 370,760" fill="var(--mist)"/>
    <line x1="300" y1="130" x2="764" y2="470" stroke="var(--teal)" stroke-width="1"/>
    <line x1="764" y1="480" x2="470" y2="1010" stroke="var(--teal)" stroke-width="1"/>
    <line x1="0" y1="760" x2="250" y2="930" stroke="var(--navy)" stroke-width="1"/>
  </svg>

  <div class="brand"><span class="brand-dot"></span>Lindenhof Kolleg</div>

  <h1 class="headline">Das<br><strong>Anonyme</strong><br>Beratungs-<br>und Begleit-<br>Angebot</h1>
  <p class="subline">für MitarbeiterInnen und Führungskräfte<br>in schwierigen Berufs- und Lebensphasen.</p>

  <p class="hotline-intro">Das LHK Beratungs-Telefon des<br>Lindenhof Kolleg für Hochschulbildung.</p>
  <div class="hotline-band">
    <svg width="30" height="30" viewBox="0 0 30 30" aria-hidden="true">
      <circle cx="15" cy="15" r="13" fill="none" stroke="#fff" stroke-width="2.5"/>
      <path d="M10 8 l3 0 l1.5 4 l-2 1.5 a9 9 0 0 0 4 4 l1.5 -2 l4 1.5 l0 3 a2 2 0 0 1 -2 2 a13 13 0 0 1 -12 -12 a2 2 0 0 1 2 -2z" fill="#fff"/>
    </svg>
    0451 – 555 27 – 140
  </div>

  <div class="hours">
    <p>Sofortberatung oder Termin-<br>vereinbarung zu Ihrer Wunschzeit</p>
    <p>Di. 14:00 – 17:00 Uhr<br>Do. 9:00 – 12:00 Uhr</p>
  </div>

  <p class="audience">Für wen?<br>Für alle Mitarbeitenden und Führungskräfte der Hochschule Lindenhof</p>

  <div class="bar bar-fields">Die Beratungsfelder</div>
  <section class="field field-private">
    <h3>Private Anliegen:</h3>
    <p>Partnerschaftskonflikte, Erziehungsberatung, Trennung/Scheidung, Verlust, Trauer, Todesfall, Schockdiagnosen usw.</p>
  </section>
  <section class="field field-health">
    <h3>Psychische<br>Gesundheit:</h3>
    <p>Sucht und Abhängigkeiten, Depressionen, Burnout, Ängste usw.</p>
  </section>
  <section class="field field-work">
    <h3>Berufliche Anliegen:</h3>
    <p>Vereinbarkeit Beruf und Familie, Konflikte mit Kolleginnen oder Kollegen oder Vorgesetzten, Überforderungen am Arbeitsplatz sowie Coaching für Führungskräfte.</p>
  </section>

  <div class="bar bar-process">Der Ablauf</div>
  <section class="process">
    <h3>Sie wählen 0451 555 27 140</h3>
    <p>- Ihr Anruf wird von den psychologischen Assistentinnen angenommen<br>
    - Diese erfragen ein Stichwort zu Ihrem Anliegen, um Sie<br>
    &nbsp;&nbsp;direkt mit einer Expertin oder einem Experten für Ihr Thema verbinden zu können</p>
  </section>

  <div class="bar bar-anon">Anonymität</div>
  <p class="anon-note">Die Beratung ist anonym. Sie müssen Ihren Namen nicht nennen.</p>

  <footer class="footer-band">Unsere Beraterinnen und Berater verfügen alle über langjährige Beratungserfahrung<br>und je nach Thema auch über eine Psychotherapiezulassung.</footer>
</main>
</body>
</html>
```